Onboarding Infographic/brochure

We are a small criminal defense firm looking to create some sort of infographic or brochure that we can onboard new clients with. We are currently sending it out via email but want something a bit cooler and fun to send to clients. The information is:

A Few Quick Rules

We are here to help each step of the way. While questions are never discouraged, this letter will answer some of the most common ones we get asked.

Communications

As a client, you should always be in the loop. While we will try to respond to questions as quickly as possible, sometimes we are unable to respond right away. Do not worry - we promise to get back to you soon. Some questions might take some time to research, and a correct answer is better than a quick one.

Appointments

One of the benefits of having an attorney is the ability to discuss your case outside of court, minus the stress and headaches. If you need an appointment, please contact the office.

Appointments must be scheduled in advance. We do not want you to make a special trip to the office only to learn that we are in court or otherwise unavailable.

Jail Visits

If your family member is currently in jail, we take that very seriously. We will visit your loved one and introduce ourselves. While the case is ongoing, we ask that a family member be designated a “contact” person so that messages can be relayed quickly. Never discuss the facts of the case over the phone with someone who is in jail. Jail calls are recorded and we have seen too many cases go south based on remarks made over recorded lines.

Police Reports and Discovery

We will do our best to provide you with copies of everything we receive on your case. Most information will be emailed, so please keep your email address up to date.

Changes in Contact Information

If you move or change numbers during the case, please let us know. It is difficult to help if we are unable to reach you, and helping you is why we are here.

Court Appearances

Cases do not get resolved as quickly as they do on television. Expect there to be several hearings in your case and it may be necessary for you to attend one or more of them. If a hearing is set, you will receive notice of the date and time of each hearing.

Billing and Collections

We understand that this investment was a huge decision for you. As we focus on providing the best representation, we will need for you to stay on schedule with any payment arrangements agreed to at the time of your initial consultation.

Again, thank you for your trust in us. We look forward to getting a fantastic outcome on your case.

Target Market(s)

Criminal defense clients and their families

Industry/Entity Type

Legal

Font styles to use
Serif

Requirements
Must have
• Must incorporate all of the rules we email out. Would like diagrams, images or pictures
Nice to have
• We attached a Welcome brochure. Not sure I want it to look super similar, hence the request for infographic.

```html
<!DOCTYPE html>
<html lang="en">
<head>
<meta charset="utf-8">
<title>Harborline Legal Group – A Few Quick Rules</title>
<link href="https://fonts.googleapis.com/css2?family=Montserrat:ital,wght@0,400;0,500;0,600;0,700;0,800;0,900;1,600&family=Pinyon+Script&display=swap" rel="stylesheet">
<style>
  :root{
    --navy:#0b2463;
    --royal:#0a4fb5;
    --sky:#afc8e6;
    --ice:#9fc0ea;
    --ink:#12224e;
    --white:#ffffff;
  }
  *{margin:0;padding:0;box-sizing:border-box}
  html,body{width:1200px;height:3600px;overflow:hidden;background:var(--sky)}
  body{font-family:"Montserrat",sans-serif;color:var(--ink);position:relative}

  .hero-photo{position:absolute;left:0;top:0;width:1200px;height:700px;
    background:linear-gradient(180deg,#5a6a8f 0%,#a7573f 30%,#8a4a2c 55%,#c9b8a6 85%,#d9cfc4 100%)}
  .hero-curve{position:absolute;left:0;top:500px;width:1200px;height:400px}
  .brand-top{position:absolute;right:44px;top:52px;text-align:right;color:var(--white);
    font-weight:800;font-size:56px;line-height:1;letter-spacing:1px}
  .brand-top small{display:block;font-size:24px;font-weight:800;letter-spacing:12px;margin-top:8px}
  .hero-title{position:absolute;left:44px;top:440px;
    font-weight:900;font-size:106px;letter-spacing:-1px;color:var(--navy);
    -webkit-text-stroke:2px var(--ice);paint-order:stroke fill;white-space:nowrap}

  .intro{position:absolute;left:49px;top:718px;width:960px}
  .intro h1{font-weight:700;font-size:57px;color:var(--navy);letter-spacing:.5px}
  .intro p{font-style:italic;font-weight:600;font-size:28px;line-height:34px;color:var(--navy);margin-top:12px}

  .rule{position:absolute;left:0;width:1200px}
  .rule-bar{height:77px;width:664px;background:var(--navy);border-radius:0 39px 39px 0;
    display:flex;align-items:center;gap:16px;padding:0 40px 0 30px;color:var(--white)}
  .rule-bar.wide{width:845px;padding-right:22px;padding-left:28px}
  .rule-bar h2{flex:1;font-weight:600;font-size:42px;letter-spacing:.2px;white-space:nowrap}
  .rule-bar.wide h2{letter-spacing:-.3px}
  .rule-bar svg{width:56px;height:56px;flex:none}
  .rule-body{margin:16px 0 0 59px;width:1020px;font-size:24.5px;line-height:39.5px;text-align:justify}
  .rule-body p+p{margin-top:8px}

  .attorney-photo{position:absolute;left:0;top:2794px;width:575px;height:486px;
    background:linear-gradient(90deg,#d57a55 0%,#d9c8bb 22%,#b8c9e3 40%,#5b5f68 60%,#6f737c 100%)}
  .thanks{position:absolute;left:605px;top:2895px;width:540px;font-family:"Pinyon Script",cursive;
    font-size:40px;line-height:52px;color:var(--navy)}
  .signature{position:absolute;left:845px;top:3122px;width:280px;height:92px;
    background:rgba(11,36,99,.12);border-radius:6px}

  .footer{position:absolute;left:0;top:3280px;width:1200px;height:320px;background:var(--navy);color:var(--white)}
  .footer-brand{position:absolute;left:95px;top:68px;font-weight:800;font-size:44px;line-height:50px;letter-spacing:1px}
  .footer-contact{position:absolute;right:46px;top:20px;text-align:right}
  .footer-contact h3{font-weight:500;font-size:45px;color:var(--ice);margin-bottom:6px}
  .footer-contact p{font-size:29px;line-height:34.5px}
  .footer-rule{position:absolute;left:112px;top:243px;width:976px;height:1px;background:rgba(255,255,255,.45)}
  .footer-web{position:absolute;left:0;top:260px;width:1200px;text-align:center;font-size:25px;letter-spacing:17px}
</style>
</head>
<body>

<div class="hero-photo" role="img" aria-label="Photo of a wooden gavel in front of an American flag"></div>
<svg class="hero-curve" viewBox="0 0 1200 400" preserveAspectRatio="none" aria-hidden="true">
  <path d="M0,157 Q560,30 1200,227 L1200,400 L0,400 Z" fill="#0a4fb5"/>
  <path d="M0,164 Q600,60 1200,360 L1200,400 L0,400 Z" fill="#afc8e6"/>
</svg>
<div class="brand-top">HARBORLINE<small>LEGAL GROUP</small></div>
<div class="hero-title">CRIMINAL DEFENSE</div>

<section class="intro">
  <h1>A FEW QUICK RULES</h1>
  <p>We are here to help each step of the way. While questions are never discouraged, this letter will answer some of the most common ones we get asked.</p>
</section>

<section class="rule" style="top:953px">
  <div class="rule-bar" style="padding-left:49px"><h2>Communications</h2>
    <svg viewBox="0 0 48 48" fill="none" stroke="#fff" stroke-width="3"><circle cx="12" cy="10" r="5" fill="#fff"/><circle cx="36" cy="28" r="5" fill="#fff"/><path d="M4 26h16M28 44h16M22 10h16v8M34 16l4 4 4-4M26 38H10v-8M14 32l-4-4-4 4"/></svg>
  </div>
  <div class="rule-body"><p>As a client, you should always be in the loop. While we will try to respond to questions as quickly as possible, sometimes we are unable to respond right away. Do not worry - we promise to get back to you soon. Some questions might take some time to research, and a correct answer is better than a quick one.</p></div>
</section>

<section class="rule" style="top:1218px">
  <div class="rule-bar"><h2>Appointments</h2>
    <svg viewBox="0 0 48 48" fill="none" stroke="#fff" stroke-width="3"><rect x="5" y="9" width="38" height="34" rx="3"/><path d="M5 18h38M14 4v9M34 4v9"/><path d="M12 25h4M22 25h4M32 25h4M12 32h4M22 32h4M32 32h4M12 38h4M22 38h4" stroke-width="3.5"/></svg>
  </div>
  <div class="rule-body"><p>One of the benefits of having an attorney is the ability to discuss your case outside of court, minus the stress and headaches. If you need an appointment, please contact the office.</p><p>Appointments must be scheduled in advance. We do not want you to make a special trip to the office only to learn that we are in court or otherwise unavailable.</p></div>
</section>

<section class="rule" style="top:1531px">
  <div class="rule-bar"><h2>Jail Visits</h2>
    <svg viewBox="0 0 48 48" fill="none" stroke="#fff" stroke-width="3"><rect x="8" y="4" width="32" height="40"/><path d="M4 44h40M16 4v40M24 4v12M24 32v12M32 4v40"/><rect x="19" y="18" width="10" height="12" fill="#fff"/></svg>
  </div>
  <div class="rule-body"><p>If your family member is currently in jail, we take that very seriously. We will visit your loved one and introduce ourselves. While the case is ongoing, we ask that a family member be designated a “contact” person so that messages can be relayed quickly. Never discuss the facts of the case over the phone with someone who is in jail. Jail calls are recorded and we have seen too many cases go south based on remarks made over recorded lines.</p></div>
</section>

<section class="rule" style="top:1875px">
  <div class="rule-bar wide"><h2>Police Reports and Discovery</h2>
    <svg viewBox="0 0 48 48" fill="none" stroke="#fff" stroke-width="3"><path d="M4 8h14l4 3v26l-4-3H4zM40 8H26l-4 3"/><circle cx="32" cy="30" r="8"/><path d="M38 36l7 7" stroke-width="4"/><path d="M8 16h8M8 22h8M8 28h8"/></svg>
  </div>
  <div class="rule-body"><p>We will do our best to provide you with copies of everything we receive on your case. Most information will be emailed, so please keep your email address up to date.</p></div>
</section>

<section class="rule" style="top:2096px">
  <div class="rule-bar wide"><h2>Changes in Contact Information</h2>
    <svg viewBox="0 0 48 48" fill="none" stroke="#fff" stroke-width="3"><circle cx="22" cy="26" r="13"/><path d="M9 26h26M22 13c-6 7-6 19 0 26M22 13c6 7 6 19 0 26"/><path d="M30 6a18 18 0 0 1 12 20M38 20l4 6 5-5"/></svg>
  </div>
  <div class="rule-body"><p>If you move or change numbers during the case, please let us know. It is difficult to help if we are unable to reach you, and helping you is why we are here.</p></div>
</section>

<section class="rule" style="top:2288px">
  <div class="rule-bar"><h2>Court Appearances</h2>
    <svg viewBox="0 0 48 48" fill="#fff" stroke="#fff" stroke-width="3"><path d="M24 4L6 14h36z"/><path d="M12 20v18M20 20v18M28 20v18M36 20v18" fill="none"/><path d="M6 42h36M8 18h32" fill="none"/></svg>
  </div>
  <div class="rule-body"><p>Cases do not get resolved as quickly as they do on television. Expect there to be several hearings in your case and it may be necessary for you to attend one or more of them. If a hearing is set, you will receive notice of the date and time of each hearing.</p></div>
</section>

<section class="rule" style="top:2557px">
  <div class="rule-bar"><h2>Billing and Collections</h2>
    <svg viewBox="0 0 48 48" fill="#fff"><ellipse cx="30" cy="10" rx="14" ry="5"/><rect x="16" y="14" width="28" height="6" rx="3"/><rect x="16" y="22" width="28" height="6" rx="3"/><rect x="16" y="30" width="28" height="6" rx="3"/><rect x="16" y="38" width="28" height="6" rx="3"/><circle cx="12" cy="32" r="9"/></svg>
  </div>
  <div class="rule-body"><p>We understand that this investment was a huge decision for you. As we focus on providing the best representation, we will need for you to stay on schedule with any payment arrangements agreed to at the time of your initial consultation.</p></div>
</section>

<div class="attorney-photo" role="img" aria-label="Photo of the firm's attorney in a grey suit leaning on a stone column"></div>
<p class="thanks">Again, thank you for your trust in us. We look forward to getting a fantastic outcome on your case.</p>
<div class="signature" role="img" aria-label="Attorney's handwritten signature"></div>

<footer class="footer">
  <div class="footer-brand">HARBORLINE<br>LEGAL GROUP</div>
  <div class="footer-contact">
    <h3>Calls answered 24/7</h3>
    <p>Toll free (888) 555-0142</p>
    <p>555-0142</p>
    <p>(909) 555-0142</p>
    <p>info@harborlinelegal.com</p>
  </div>
  <div class="footer-rule"></div>
  <div class="footer-web">WWW.HARBORLINELEGAL.COM</div>
</footer>

</body>
</html>
```